Bref créative
Stationary for Visual Explanation Business
Bus Card, Stationary
Professional
Martin Pelloway
CEO & Founder
487 E 29th Street, Suite 4B
New York, NY 10027
USA
martin@lumbrivista.com
www.lumbrivista.com
Looking for clean and modern sophisticated look and feel for a marketing service business company that offers visual explanations for technology companies. Not cutesy. A blend of QXR combined with creative agency.
The letterhead will serve as my proposal template. I will use it for placing text and illustrations.
I want to keep with the orange and gray of the logo.
I wil supply the AI version of the logo shortly.
Logo AI File with tagline and name
Logo Ai File with company name and no tagline
Logo Ai file with no tagline and no company name

```html
<!DOCTYPE html>
<html lang="en">
<head>
<meta charset="utf-8">
<title>LumbriVista Business Card</title>
<link href="https://fonts.googleapis.com/css2?family=Arimo:wght@400;700&display=swap" rel="stylesheet">
<style>
  :root {
    --orange: #f7941d;
    --slate: #6b7174;
    --ink: #5f6366;
    --paper: #ffffff;
    --edge: #3a3a3a;
  }
  * { margin: 0; padding: 0; box-sizing: border-box; }
  html, body {
    width: 1200px; height: 751px; overflow: hidden;
    background: var(--paper);
    font-family: "Arimo", Arial, sans-serif;
  }
  .card {
    position: absolute; left: 72px; top: 77px;
    width: 1056px; height: 602px;
    border: 2px solid var(--edge);
    background: var(--paper);
  }
  .band { position: absolute; left: 0; width: 1200px; height: 24px; }
  .band--top { top: 106px; }
  .band--bottom { top: 618px; }
  .band rect { fill: var(--slate); }

  .brand {
    position: absolute; left: 96px; top: 330px;
    display: flex; align-items: center; gap: 22px;
  }
  .brand__square {
    width: 84px; height: 84px; background: var(--orange);
  }
  .brand__name {
    font-size: 54px; font-weight: 700; color: var(--slate);
    letter-spacing: -1px;
  }

  .contact {
    position: absolute; left: 698px; top: 222px;
    font-weight: 700;
  }
  .contact__name { font-size: 41px; color: var(--orange); line-height: 1.05; }
  .contact__role { font-size: 32px; color: var(--ink); line-height: 1.15; }
  .contact__details {
    margin-top: 68px; list-style: none;
    font-size: 25px; color: var(--ink); line-height: 31px;
  }
</style>
</head>
<body>
  <div class="card"></div>

  <svg class="band band--top" viewBox="0 0 1200 24" aria-hidden="true">
    <rect x="74" y="0" width="44" height="24"/>
    <rect x="130" y="0" width="44" height="24"/>
    <rect x="186" y="0" width="44" height="24"/>
    <rect x="242" y="0" width="44" height="24"/>
    <rect x="294" y="0" width="40" height="24"/>
    <rect x="344" y="0" width="782" height="24"/>
  </svg>

  <svg class="band band--bottom" viewBox="0 0 1200 24" aria-hidden="true">
    <rect x="74" y="0" width="778" height="24"/>
    <rect x="864" y="0" width="43" height="24"/>
    <rect x="919" y="0" width="42" height="24"/>
    <rect x="972" y="0" width="43" height="24"/>
    <rect x="1027" y="0" width="42" height="24"/>
    <rect x="1080" y="0" width="46" height="24"/>
  </svg>

  <div class="brand">
    <div class="brand__square"></div>
    <div class="brand__name">LumbriVista</div>
  </div>

  <div class="contact">
    <div class="contact__name">Martin Pelloway</div>
    <div class="contact__role">CEO &amp; Founder</div>
    <ul class="contact__details">
      <li>487 E 29th Street, Suite 4B</li>
      <li>New York, NY 10027</li>
      <li>Phone: (917) 555-0148</li>
      <li>martin@lumbrivista.com</li>
      <li>www.lumbrivista.com</li>
    </ul>
  </div>
</body>
</html>
```